Breezeway Comfort business cards design

Need a business card design for a Heating and Air Conditioning business. I need these items included.
Business name: Breezeway Comfort
Owner: Marcus Tollefsen
License # 2874590
Phone number # 555-382-4071
Email: breezewaycomfortair@mailvista.example
Sales
Service
Installation
Maintenance

Heating and Air Conditioning

Requirements
Must have
• Company name , license number , phone number , email

```html
<!DOCTYPE html>
<html lang="en">
<head>
<meta charset="utf-8">
<title>Breezeway Comfort – Business Cards</title>
<link rel="stylesheet" href="https://fonts.googleapis.com/css2?family=Orbitron:wght@500;600&family=Roboto:wght@400;500&display=swap">
<style>
  :root {
    --page-bg: #d4d5d7;
    --card-white: #ffffff;
    --brand-blue: #1f4a9e;
    --brand-orange: #ef6a3c;
    --text-grey: #555a60;
    --back-blue: #1f4698;
    --back-blue-deep: #1a3b86;
    --back-name: #7fa8ea;
  }
  * { margin: 0; padding: 0; box-sizing: border-box; }
  html, body { width: 1200px; height: 1000px; overflow: hidden; }
  body { background: var(--page-bg); position: relative; font-family: "Roboto", sans-serif; }

  .card { position: absolute; left: 277px; width: 602px; height: 344px; }
  .card-front { top: 118px; background: var(--card-white); box-shadow: 0 2px 8px rgba(0,0,0,0.12); }
  .card-back { top: 573px; background: linear-gradient(135deg, var(--back-blue), var(--back-blue-deep)); box-shadow: 0 2px 8px rgba(0,0,0,0.15); }

  .brand-block {
    position: absolute; left: 56px; top: 124px; width: 216px;
    display: flex; align-items: center; gap: 10px;
  }
  .brand-dot { width: 18px; height: 18px; border-radius: 50%; background: var(--brand-orange); flex: none; }
  .brand-name {
    font-family: "Orbitron", sans-serif; font-weight: 600; font-size: 21px;
    line-height: 1.2; color: var(--brand-blue); text-transform: uppercase;
  }

  .divider { position: absolute; left: 287px; top: 86px; width: 2px; height: 152px; background: var(--brand-blue); }

  .contact { position: absolute; left: 309px; top: 84px; }
  .owner-name {
    font-family: "Orbitron", sans-serif; font-weight: 600; font-size: 16px;
    color: var(--brand-blue); letter-spacing: 0.5px; text-transform: uppercase;
  }
  .owner-role { font-weight: 500; font-size: 15px; color: var(--brand-orange); margin-top: 2px; }
  .address { font-size: 14px; color: var(--text-grey); line-height: 18px; margin-top: 10px; }
  .contact-line { display: flex; align-items: center; gap: 7px; font-size: 14px; color: var(--text-grey); margin-top: 4px; white-space: nowrap; }
  .contact-line svg { width: 14px; height: 14px; flex: none; }
  .contact-line.first { margin-top: 7px; }
  .license { font-size: 13px; color: var(--text-grey); margin-top: 4px; }
  .license strong { font-weight: 500; color: var(--brand-blue); }

  .services {
    position: absolute; left: 0; right: 0; top: 290px;
    display: flex; justify-content: center; gap: 10px;
    font-family: "Orbitron", sans-serif; font-weight: 500; font-size: 13px;
    color: var(--brand-blue); letter-spacing: 0.6px; text-transform: uppercase;
  }
  .service { display: flex; align-items: center; gap: 6px; }
  .service-mark { width: 12px; height: 12px; background: var(--brand-orange); }

  .back-brand {
    position: absolute; left: 0; right: 0; top: 118px;
    display: flex; justify-content: center; align-items: center; gap: 16px;
  }
  .back-dot { width: 30px; height: 30px; border-radius: 50%; background: var(--back-name); flex: none; }
  .back-text { display: flex; flex-direction: column; align-items: center; }
  .back-name {
    font-family: "Orbitron", sans-serif; font-weight: 600; font-size: 32px;
    color: var(--back-name); text-transform: uppercase; letter-spacing: 1px; line-height: 1.15;
  }
  .back-tagline {
    font-family: "Orbitron", sans-serif; font-weight: 500; font-size: 19px;
    color: var(--brand-orange); text-transform: uppercase; letter-spacing: 4px; margin-top: 8px;
  }
</style>
</head>
<body>
  <section class="card card-front">
    <div class="brand-block">
      <span class="brand-dot"></span>
      <span class="brand-name">Breezeway<br>Comfort</span>
    </div>
    <div class="divider"></div>
    <div class="contact">
      <p class="owner-name">Marcus Tollefsen</p>
      <p class="owner-role">Owner</p>
      <p class="address">48 Harbour Ridge Lane<br>Maple Grove, ON L7K</p>
      <p class="contact-line first">
        <svg viewBox="0 0 16 16" aria-hidden="true"><path fill="#ef6a3c" d="M2 5c0-2 2-3 6-3s6 1 6 3v1h-3V5H5v1H2zM4 8h8l2 6H2z"/></svg>
        555-382-4071
      </p>
      <p class="contact-line">
        <svg viewBox="0 0 16 16" aria-hidden="true"><rect x="1" y="3" width="14" height="10" rx="1" fill="#ef6a3c"/><path d="M1.5 4L8 9l6.5-5" stroke="#fff" stroke-width="1.4" fill="none"/></svg>
        breezewaycomfortair@mailvista.example
      </p>
      <p class="license"><strong>License #</strong> 2874590</p>
    </div>
    <div class="services">
      <span class="service"><span class="service-mark"></span>Sales</span>
      <span class="service"><span class="service-mark"></span>Service</span>
      <span class="service"><span class="service-mark"></span>Installation</span>
      <span class="service"><span class="service-mark"></span>Maintenance</span>
    </div>
  </section>

  <section class="card card-back">
    <div class="back-brand">
      <span class="back-dot"></span>
      <div class="back-text">
        <span class="back-name">Breezeway Comfort</span>
        <span class="back-tagline">Heating &amp; Air Conditioning</span>
      </div>
    </div>
  </section>
</body>
</html>
```